Motivational Poster Design Project

I would like to create a poster with some of my favorite quotes to hang in my office.

Industry/Entity Type

Quotes

Requirements
Must have
• The poster will be 24" high x 36" long and printed on canvas, so the image you create needs to have a resolution of at least 2700 x 3900.

The poster must contain the following quotes:

“Your beliefs become your thoughts,
Your thoughts become your words,
Your words become your actions,
Your actions become your habits,
Your habits become your values,
Your values become your destiny.”
-Varuna Pellath

"Winners practice until they get it right. Champions practice until they can’t get it wrong!"
-Unknown

"Style is the perfection of a point of view."
-Conrad Whitlowe

"My interest in life comes from setting myself huge, apparently unachieveable challenges and trying to rise above them."
-Sir Oswin Talbrook

"Problems cannot be solved by the same level of thinking that created them."
-Gustav Morrendel

"People think focus means saying yes to the thing you've got to focus on. But that's not what it means at all. It means saying no to the hundred other good ideas that there are. You have to pick carefully."
-Dale Parrick

"Think like a man of action and act like a man of thought."
-Lucien Marvaud
Nice to have
• It would be nice to have an image of each person who is being quoted (if known) along with the quote that is attributable to them.

```html
<!DOCTYPE html>
<html lang="en">
<head>
<meta charset="utf-8">
<title>Quote Tree Poster</title>
<link href="https://fonts.googleapis.com/css2?family=Cormorant+Garamond:ital,wght@1,400&family=Josefin+Sans:wght@400&display=swap" rel="stylesheet">
<style>
  :root {
    --paper: #ffffff;
    --tree: #f3e9e0;
    --ink: #7a4a26;
    --photo-light: #d9c8b6;
    --photo-dark: #6e4b30;
  }
  html, body { margin: 0; padding: 0; overflow: hidden; background: var(--paper); }
  .poster {
    position: relative;
    width: 800px;
    height: 1200px;
    overflow: hidden;
    background: var(--paper);
  }
  .tree-art {
    position: absolute;
    left: 0; top: 110px;
    width: 800px; height: 1090px;
    background: radial-gradient(ellipse 62% 48% at 50% 40%, var(--tree) 0%, rgba(243,233,224,0.55) 55%, rgba(255,255,255,0) 100%);
  }
  .portrait {
    position: absolute;
    width: 104px; height: 104px;
    border-radius: 50%;
    background: radial-gradient(circle at 45% 40%, var(--photo-light) 0%, #a8876a 55%, var(--photo-dark) 100%);
  }
  .portrait--pale { background: radial-gradient(circle at 50% 45%, #eee6dc 0%, #ddd0c2 70%, #cbb9a6 100%); }
  .quote {
    position: absolute;
    width: 440px;
    margin: 0;
    text-align: center;
    font-family: "Cormorant Garamond", serif;
    font-style: italic;
    font-size: 15px;
    line-height: 18px;
    letter-spacing: -0.02em;
    color: var(--ink);
  }
  .author {
    position: absolute;
    width: 440px;
    margin: 0;
    text-align: center;
    font-family: "Josefin Sans", sans-serif;
    font-size: 10.5px;
    letter-spacing: 0.3em;
    text-transform: uppercase;
    color: var(--ink);
  }
</style>
</head>
<body>
<main class="poster">
  <div class="tree-art" role="img" aria-label="Large pale bare tree with spreading branches"></div>

  <div class="portrait" style="left:164px;top:128px" role="img" aria-label="Portrait photo of Gustav Morrendel"></div>
  <p class="quote" style="left:-4px;top:233px">Problems cannot be solved<br>by the same level of thinking that created them</p>
  <p class="author" style="left:-4px;top:281px">Gustav Morrendel</p>

  <div class="portrait portrait--pale" style="left:600px;top:180px" role="img" aria-label="Misty seascape photo"></div>
  <p class="quote" style="left:432px;top:291px">Winners practice until they get it right.<br>Champions practice until they can’t get it wrong</p>
  <p class="author" style="left:432px;top:336px">Unknown</p>

  <div class="portrait" style="left:370px;top:312px" role="img" aria-label="Portrait photo of Varuna Pellath"></div>
  <p class="quote" style="left:202px;top:429px">Your beliefs become your thoughts, Your thoughts become your words,<br>Your words become your actions, Your actions become your habits,<br>Your habits become your values, Your values become your destiny</p>
  <p class="author" style="left:202px;top:493px">Varuna Pellath</p>

  <div class="portrait" style="left:90px;top:462px" role="img" aria-label="Portrait photo of Conrad Whitlowe"></div>
  <p class="quote" style="left:-78px;top:579px">Style is the perfection of a point of view</p>
  <p class="author" style="left:-78px;top:607px">Conrad Whitlowe</p>

  <div class="portrait" style="left:554px;top:526px" role="img" aria-label="Portrait photo of Dale Parrick"></div>
  <p class="quote" style="left:386px;top:642px">People think focus means saying yes to the thing<br>you’ve got to focus on. But that’s not what it means at all.<br>It means saying no to the hundred other good ideas that there are.<br>You have to pick carefully</p>
  <p class="author" style="left:386px;top:728px">Dale Parrick</p>

  <div class="portrait" style="left:148px;top:674px" role="img" aria-label="Portrait photo of Lucien Marvaud"></div>
  <p class="quote" style="left:-20px;top:787px">Think like a man of action and act like a man of thought</p>
  <p class="author" style="left:-20px;top:816px">Lucien Marvaud</p>

  <div class="portrait" style="left:529px;top:778px" role="img" aria-label="Portrait photo of Sir Oswin Talbrook"></div>
  <p class="quote" style="left:361px;top:895px">My interest in life comes from setting myself huge,<br>apparently unachieveable challenges and trying<br>to rise above them</p>
  <p class="author" style="left:361px;top:958px">Sir Oswin Talbrook</p>
</main>
</body>
</html>
```